Coastal Bright Sweep Business Card

We are a cleaning and waste management company with the slogan "making waste to landfill a thing of the past". We would like a re-design of our current business card. On the front we want to continue to use our logo as the focus point. On the back, we want the whole thing re-done to be less busy. We want the staff member’s name, the job title, mobile number, email and website. We do not want the address on the card. We still want the green, black and blue colours used, but a new font for the information on the back. Please do not change the logo design at all. We are also thinking about using icons to replace the text ‘mobile, email, website’. The “events + commercial” banner needs to be incorporated somewhere and needs to read “events + commercial + waste”. Another important point for consideration is that we are very concerned about being environmentally sustainable and will be printing on recycled paper. All designs should be made to compliment this in regards to boldness and colouring. Please find attached our logo, our colour chart and an image of our current business card.

```html
<!DOCTYPE html>
<html lang="en">
<head>
<meta charset="UTF-8">
<title>Coastal Bright Sweep – Business Card</title>
<link href="https://fonts.googleapis.com/css2?family=Raleway:wght@400;500;800&display=swap" rel="stylesheet">
<style>
  :root {
    --navy: #12406f;
    --navy-deep: #0f3a6b;
    --green: #7ac143;
    --blue: #2aa4e0;
    --sky: #a9d6e0;
    --sky-deep: #8ecad8;
    --ink: #2b2b2b;
    --paper: #ffffff;
    --backdrop: #d9d9d9;
  }
  * { box-sizing: border-box; margin: 0; padding: 0; }
  html, body { width: 1200px; height: 1200px; overflow: hidden; }
  body {
    background: var(--backdrop);
    font-family: "Raleway", Arial, sans-serif;
    position: relative;
  }
  .card {
    position: absolute;
    left: 238px;
    width: 724px;
    height: 436px;
    box-shadow: 0 18px 30px rgba(0,0,0,0.25);
  }

  /* Brand name placeholder */
  .brand-name {
    position: absolute;
    font-weight: 800;
    color: var(--navy);
    text-transform: uppercase;
    text-align: center;
    line-height: 1.05;
  }

  /* Front */
  .card--front { top: 105px; background: var(--paper); padding: 26px; }
  .front__photo {
    width: 100%; height: 100%;
    background: radial-gradient(ellipse 48% 62% at 46% 50%, #ffffff 0%, #ffffff 55%, var(--sky) 85%, var(--sky-deep) 100%);
    position: relative;
  }
  .card--front .brand-name { left: 162px; top: 118px; width: 340px; font-size: 46px; }

  /* Back */
  .card--back { top: 630px; background: var(--navy-deep); padding: 28px 28px 26px 28px; }
  .back__panel { width: 100%; height: 100%; background: var(--paper); position: relative; }
  .staff__name {
    position: absolute; left: 19px; top: 25px;
    font-size: 30px; font-weight: 800; color: var(--green); letter-spacing: 0.5px;
  }
  .staff__title {
    position: absolute; left: 19px; top: 62px;
    font-size: 21px; font-weight: 400; color: var(--ink);
  }
  .card--back .brand-name { right: 28px; top: 30px; width: 260px; font-size: 38px; }

  .contacts { position: absolute; left: 16px; bottom: 16px; list-style: none; }
  .contacts__item {
    display: flex; align-items: center; gap: 9px;
    font-size: 17px; color: var(--ink); height: 30px;
  }
  .contacts__icon { width: 21px; height: 21px; flex: none; }

  .services { position: absolute; right: 20px; bottom: 14px; list-style: none; text-align: right; }
  .services__item {
    font-size: 22px; font-weight: 500; color: var(--ink);
    padding: 4px 0 6px 0; width: 170px; margin-left: auto;
  }
  .services__item + .services__item { border-top: 2px dotted var(--blue); }
</style>
</head>
<body>

  <section class="card card--front">
    <div class="front__photo" role="img" aria-label="Photo of a gloved hand wiping a light blue surface clean with a cloth">
      <div class="brand-name">Coastal<br>Bright Sweep</div>
    </div>
  </section>

  <section class="card card--back">
    <div class="back__panel">
      <h1 class="staff__name">MORGAN ELLERY</h1>
      <p class="staff__title">Client Manager</p>

      <div class="brand-name">Coastal<br>Bright<br>Sweep</div>

      <ul class="contacts">
        <li class="contacts__item">
          <svg class="contacts__icon" viewBox="0 0 24 24" aria-hidden="true"><rect x="6" y="1.5" width="12" height="21" rx="2" fill="none" stroke="var(--green)" stroke-width="2"/><circle cx="12" cy="19" r="1.2" fill="var(--green)"/></svg>
          0400 555 218
        </li>
        <li class="contacts__item">
          <svg class="contacts__icon" viewBox="0 0 24 24" aria-hidden="true"><rect x="1.5" y="5" width="21" height="14" fill="var(--green)"/><path d="M1.5 5 L12 13 L22.5 5 M1.5 19 L9 11.5 M22.5 19 L15 11.5" fill="none" stroke="#fff" stroke-width="1.5"/></svg>
          mellery@coastalbrightsweep.com.au
        </li>
        <li class="contacts__item">
          <svg class="contacts__icon" viewBox="0 0 24 24" aria-hidden="true"><g fill="none" stroke="var(--green)" stroke-width="1.6"><circle cx="12" cy="12" r="10"/><ellipse cx="12" cy="12" rx="4.5" ry="10"/><path d="M2 12 H22 M4 6.5 H20 M4 17.5 H20"/></g></svg>
          www.coastalbrightsweep.com.au
        </li>
      </ul>

      <ul class="services">
        <li class="services__item">EVENTS</li>
        <li class="services__item">COMMERCIAL</li>
        <li class="services__item">WASTE</li>
      </ul>
    </div>
  </section>

</body>
</html>
```